" Escritório de Advocacia, com 05 anos de atuaçao em diversas áreas do direito, em especial direito civil, criminal, familia, trabalhista e comercial. Contamos com 03 advogados e alguns estagiários. "

```html
<!DOCTYPE html>
<html lang="pt-BR">
<head>
<meta charset="UTF-8">
<title>Moreira Valadares Advocacia — Cartão de visitas</title>
<link rel="stylesheet" href="https://fonts.googleapis.com/css2?family=Raleway:wght@300;400;500&display=swap">
<style>
  :root {
    --brown: #2f1f19;
    --brown-deep: #24170f;
    --gold: #b8924a;
    --gold-light: #d9b86e;
    --silver: #ececec;
    --silver-dark: #c9c9c9;
    --page: #e4e4e4;
    --ink: #3a2a22;
  }
  * { box-sizing: border-box; margin: 0; padding: 0; }
  html, body { width: 1200px; height: 1200px; overflow: hidden; }
  body {
    background: var(--page);
    font-family: "Raleway", sans-serif;
    position: relative;
  }

  .card {
    position: absolute;
    width: 520px;
    height: 290px;
    overflow: hidden;
    box-shadow: 0 10px 24px rgba(0,0,0,.18);
  }

  /* Front */
  .card-front { left: 50px; top: 190px; background: var(--brown); }
  .card-front .gold-bar {
    position: absolute; right: 60px; top: 0;
    width: 150px; height: 7px;
    background: linear-gradient(90deg, var(--gold), var(--gold-light), var(--gold));
  }
  .brand { display: flex; align-items: center; gap: 14px; }
  .brand-square {
    width: 38px; height: 38px;
    border: 2px solid var(--gold);
  }
  .brand-text { display: flex; flex-direction: column; }
  .brand-name {
    color: var(--gold);
    font-weight: 400;
    letter-spacing: .04em;
    text-transform: uppercase;
    white-space: nowrap;
  }
  .brand-tag {
    color: var(--gold);
    font-weight: 300;
    letter-spacing: .35em;
    text-transform: uppercase;
    text-align: center;
  }
  .card-front .brand { position: absolute; left: 70px; top: 105px; }
  .card-front .brand-name { font-size: 26px; }
  .card-front .brand-tag { font-size: 8px; margin-top: 4px; }
  .card-front .website {
    position: absolute; left: 70px; bottom: 34px;
    color: var(--gold); font-size: 10px; letter-spacing: .05em;
  }

  /* Back */
  .card-back { left: 630px; top: 190px; background: var(--silver); }
  .card-back .band-top {
    position: absolute; left: 0; top: 0; width: 100%; height: 92px;
    background: var(--brown);
  }
  .card-back .band-bottom {
    position: absolute; left: 0; bottom: 0; width: 100%; height: 40px;
    background: var(--brown);
  }
  .card-back .gold-bar {
    position: absolute; left: 210px; bottom: 40px;
    width: 120px; height: 5px;
    background: linear-gradient(90deg, var(--gold), var(--gold-light), var(--gold));
  }
  .card-back .mono-square {
    position: absolute; left: 40px; top: 28px;
    width: 34px; height: 34px; border: 2px solid var(--gold);
  }
  .holder {
    position: absolute; right: 40px; top: 30px;
    color: #f1e8dc; text-align: left;
  }
  .holder-name { font-size: 15px; font-weight: 400; }
  .holder-id { font-size: 12px; font-weight: 300; margin-top: 4px; }

  .contacts {
    position: absolute; left: 40px; top: 112px;
    list-style: none; color: var(--ink); font-size: 10.5px;
  }
  .contacts li { display: flex; align-items: center; gap: 8px; margin-bottom: 10px; }
  .contacts svg { width: 12px; height: 12px; fill: var(--ink); }

  .address {
    position: absolute; left: 250px; top: 150px;
    display: flex; gap: 8px; color: var(--ink); font-size: 10.5px; line-height: 1.45;
  }
  .address svg { width: 12px; height: 15px; fill: var(--ink); flex: none; margin-top: 2px; }

  /* Lockup */
  .lockup { position: absolute; left: 50%; top: 700px; transform: translateX(-50%); }
  .lockup .brand-square { width: 64px; height: 64px; border-width: 3px; }
  .lockup .brand-name { font-size: 40px; color: #8a6b34; }
  .lockup .brand-tag { font-size: 12px; margin-top: 6px; color: #8a6b34; }
  .lockup .brand-square { border-color: #8a6b34; }
</style>
</head>
<body>

  <section class="card card-front">
    <div class="gold-bar"></div>
    <div class="brand">
      <div class="brand-square"></div>
      <div class="brand-text">
        <span class="brand-name">Moreira Valadares</span>
        <span class="brand-tag">Advocacia</span>
      </div>
    </div>
    <p class="website">www.moreiravaladares.com.br</p>
  </section>

  <section class="card card-back">
    <div class="band-top"></div>
    <div class="mono-square"></div>
    <div class="holder">
      <p class="holder-name">Nome Sobrenome</p>
      <p class="holder-id">OAB 22.345</p>
    </div>

    <ul class="contacts">
      <li>
        <svg viewBox="0 0 24 24"><path d="M6.6 10.8a15.1 15.1 0 0 0 6.6 6.6l2.2-2.2a1 1 0 0 1 1-.25 11.4 11.4 0 0 0 3.6.57 1 1 0 0 1 1 1V20a1 1 0 0 1-1 1A17 17 0 0 1 3 4a1 1 0 0 1 1-1h3.5a1 1 0 0 1 1 1c0 1.25.2 2.45.57 3.57a1 1 0 0 1-.25 1z"/></svg>
        +55 (00) 0000.0000
      </li>
      <li>
        <svg viewBox="0 0 24 24"><path d="M7 1h10a2 2 0 0 1 2 2v18a2 2 0 0 1-2 2H7a2 2 0 0 1-2-2V3a2 2 0 0 1 2-2zm0 3v14h10V4zm5 15.5a1 1 0 1 0 0 2 1 1 0 0 0 0-2z"/></svg>
        +55 (00) 00000.0000
      </li>
      <li>
        <svg viewBox="0 0 24 24"><path d="M2 5h20v14H2zm2 2v.5l8 5 8-5V7l-8 5z"/></svg>
        email@email.com.br
      </li>
    </ul>

    <div class="address">
      <svg viewBox="0 0 24 30"><path d="M12 0a10 10 0 0 0-10 10c0 7.5 10 20 10 20s10-12.5 10-20A10 10 0 0 0 12 0zm0 14a4 4 0 1 1 0-8 4 4 0 0 1 0 8z"/></svg>
      <p>Rua Nome Sobrenome, 000 - Bairro<br>Cidade / UF - CEP: 00000-000</p>
    </div>

    <div class="gold-bar"></div>
    <div class="band-bottom"></div>
  </section>

  <div class="brand lockup">
    <div class="brand-square"></div>
    <div class="brand-text">
      <span class="brand-name">Moreira Valadares</span>
      <span class="brand-tag">Advocacia</span>
    </div>
  </div>

</body>
</html>
```